Book Cover for Christian book about open-air preaching

The book is about open-air or outdoor preaching. It is for pastors, evangelists, or any Christian who feels called to share the Gospel with crowds outside of the church. The title is "Quiet Meadows" with a subtitle of "A guide for patient gardening in the distant valley". The Bible verse reference for the title is Jeremiah 20:9. Size will be 9" high by 6"wide
Updates

Went on vacation/holiday

Target Market(s)

Christian pastors, missonaries, evangelists

Industry/Entity Type

religous

Requirements
Must have
• Meet Marlowe Indie Print Services guidelines for book covers

```html
<!DOCTYPE html>
<html lang="en">
<head>
<meta charset="utf-8">
<title>Quiet Meadows – Book Cover</title>
<link rel="stylesheet" href="https://fonts.googleapis.com/css2?family=Bebas+Neue&family=Crimson+Text:ital@1&family=Montserrat:wght@400&display=swap">
<style>
  :root {
    --page: #ffffff;
    --blue-deep: #0550a6;
    --blue-mid: #1a78d2;
    --blue-light: #8ab6fa;
    --band: #0a69cb;
    --yellow: #f9ec35;
    --white: #ffffff;
    --navy: #1d2a4a;
    --navy-soft: #3a5c96;
  }
  html, body {
    margin: 0;
    width: 1200px;
    height: 1200px;
    overflow: hidden;
    background: var(--page);
  }
  .canvas {
    position: relative;
    width: 1200px;
    height: 1200px;
  }
  .book-cover {
    position: absolute;
    left: 237px;
    top: 59px;
    width: 720px;
    height: 1080px;
    display: block;
  }
  .title { font-family: "Bebas Neue", "Oswald", sans-serif; }
  .title-top { fill: var(--yellow); }
  .title-bottom { fill: var(--white); }
  .subtitle {
    font-family: "Crimson Text", Georgia, serif;
    font-style: italic;
    fill: var(--white);
  }
  .author {
    font-family: "Montserrat", Arial, sans-serif;
    fill: var(--white);
    letter-spacing: 3px;
  }
</style>
</head>
<body>
<div class="canvas">
  <svg class="book-cover" viewBox="0 0 720 1080" xmlns="http://www.w3.org/2000/svg">
    <defs>
      <linearGradient id="cover-sky" x1="0" y1="1" x2="0.7" y2="0">
        <stop offset="0" stop-color="var(--blue-light)"/>
        <stop offset="0.45" stop-color="var(--blue-mid)"/>
        <stop offset="1" stop-color="var(--blue-deep)"/>
      </linearGradient>
      <linearGradient id="photo-subject" x1="0" y1="0" x2="0" y2="1">
        <stop offset="0" stop-color="var(--navy)"/>
        <stop offset="0.75" stop-color="var(--navy-soft)"/>
        <stop offset="1" stop-color="var(--navy-soft)" stop-opacity="0.55"/>
      </linearGradient>
      <linearGradient id="rule" x1="0" y1="0" x2="1" y2="0">
        <stop offset="0" stop-color="var(--yellow)" stop-opacity="0"/>
        <stop offset="0.15" stop-color="var(--yellow)"/>
        <stop offset="0.85" stop-color="var(--yellow)"/>
        <stop offset="1" stop-color="var(--yellow)" stop-opacity="0"/>
      </linearGradient>
    </defs>

    <rect class="cover-background" width="720" height="1080" fill="url(#cover-sky)"/>

    <rect class="cover-photo" x="250" y="635" width="190" height="378" rx="10"
          fill="url(#photo-subject)"
          role="img" aria-label="Photo of a raised hand holding a Bible against a clear blue sky"/>

    <text class="title title-top" x="60" y="213" font-size="240" textLength="592" lengthAdjust="spacingAndGlyphs">QUIET</text>
    <text class="title title-bottom" x="60" y="459" font-size="320" textLength="594" lengthAdjust="spacingAndGlyphs">MEADOWS</text>

    <rect class="subtitle-rule" x="127" y="492" width="464" height="2" fill="url(#rule)"/>
    <text class="subtitle" text-anchor="middle" font-size="38">
      <tspan x="360" y="535">A guide for patient gardening in</tspan>
      <tspan x="360" y="573">the distant valley</tspan>
    </text>
    <rect class="subtitle-rule" x="127" y="589" width="464" height="2" fill="url(#rule)"/>

    <rect class="author-band" x="0" y="1013" width="720" height="67" fill="var(--band)"/>
    <text class="author" x="360" y="1061" text-anchor="middle" font-size="40">AUTHOR NAME</text>
  </svg>
</div>
</body>
</html>
```